Business card for real estate agent / office

We're looking for a new business card. We want something that is pretty clean, modern and sleek. Something that also tells people that we are a new age company...cutting edge. Although real estate has been done a certain way the last 100 years, we have energy and vibrance. Company name is Bright Harbor Properties. info can be found here: http://www.bhprealestate.example/

needs to include: Name, title, phone number, email. our license number also needs to be displayed somewhere.

Target Market(s)

25-55 homeowners or potential homeowners

Industry/Entity Type

Business

Contact Information for Business Card

we need business card designs for real estate agent / office

Font styles to use
Serif

Requirements
Must have
• needs to include: Name, title, phone number, email. our license number also needs to be displayed somewhere and company name.
Nice to have
• placement area for photo

```html
<!DOCTYPE html>
<html lang="en">
<head>
<meta charset="utf-8">
<title>Bright Harbor Properties – Business Card</title>
<link href="https://fonts.googleapis.com/css2?family=Arimo:wght@400;700&display=swap" rel="stylesheet">
<style>
  :root {
    --brand-green: #5cff00;
    --brand-navy: #0f3a86;
    --paper: #ffffff;
    --trim: #222222;
  }
  * { margin: 0; padding: 0; box-sizing: border-box; }
  html, body {
    width: 1200px; height: 1200px; overflow: hidden;
    background: var(--paper);
    font-family: "Arimo", Arial, sans-serif;
  }
  .canvas { position: relative; width: 1200px; height: 1200px; }
  .card {
    position: absolute; left: 180px; width: 840px; height: 480px;
    border: 1px solid var(--trim); background: var(--paper); overflow: hidden;
  }
  .card--front { top: 94px; }
  .card--back { top: 626px; }
  .card__panel { position: absolute; inset: 0; width: 840px; height: 480px; }
  .card__panel path { fill: var(--brand-green); }
  .contact {
    position: absolute; left: 34px; top: 106px;
    color: var(--brand-navy); line-height: 1;
  }
  .contact__name { font-size: 33px; font-weight: 700; margin-bottom: 10px; }
  .contact__line { font-size: 27px; font-weight: 400; margin-bottom: 21px; white-space: nowrap; }
  .contact__line--title { margin-bottom: 22px; }
  .brand {
    position: absolute; display: flex; align-items: center; gap: 14px;
    color: var(--brand-navy); font-weight: 700; line-height: 1.05;
  }
  .brand__mark { background: var(--brand-green); flex: none; }
  .brand--front { left: 500px; top: 178px; font-size: 40px; }
  .brand--front .brand__mark { width: 30px; height: 30px; }
  .brand--back { left: 0; right: 0; top: 170px; justify-content: center; font-size: 58px; }
  .brand--back .brand__mark { width: 44px; height: 44px; }
</style>
</head>
<body>
<div class="canvas">
  <section class="card card--front">
    <svg class="card__panel" viewBox="0 0 840 480" aria-hidden="true">
      <path d="M0 0 H588 Q322 240 592 480 H0 Z"/>
    </svg>
    <div class="contact">
      <div class="contact__name">Daniel Morrow</div>
      <div class="contact__line contact__line--title">Real Estate Broker, Realtor, MBA</div>
      <div class="contact__line">M: 310.555.0142</div>
      <div class="contact__line">E: dan@brightharborprop.example</div>
      <div class="contact__line">W: www.brightharborprop.example</div>
      <div class="contact__line">CA BRE #02917355</div>
    </div>
    <div class="brand brand--front">
      <span class="brand__mark"></span>
      <span class="brand__name">Bright Harbor<br>Properties</span>
    </div>
  </section>

  <section class="card card--back">
    <div class="brand brand--back">
      <span class="brand__mark"></span>
      <span class="brand__name">Bright Harbor<br>Properties</span>
    </div>
  </section>
</div>
</body>
</html>
```